Willowbend Pharmacy Business Cards

I need a business card design and or template. Needs to convey a softer feel along with health and wellness. Please see attached logo and color scheme.

Industry/Entity Type

Pharmacy

Colors

Designer to choose colors to be used in the design.

Requirements
Must have
• I've added a second NEW colored logo I think I am going to go with the blue green logo.
• Needs to have the colors and feel of the logo attached.
• Dorian Kessel
• Pharmacy Manager
• willowbendpharmacy.example

```html
<!DOCTYPE html>
<html lang="en">
<head>
<meta charset="utf-8">
<title>Willowbend Pharmacy Business Cards</title>
<link href="https://fonts.googleapis.com/css2?family=Montserrat:wght@400;500;700&family=Rochester&display=swap" rel="stylesheet">
<style>
  :root {
    --bg: #e9eaec;
    --card: #ffffff;
    --ink: #5b5f66;
    --ink-soft: #6d7178;
    --green-light: #a6cf3f;
    --green: #7cbf3a;
    --green-deep: #5fae35;
    --pink: #ec5483;
    --pink-deep: #c8214f;
    --pink-soft: #f4a9c0;
  }
  * { box-sizing: border-box; margin: 0; padding: 0; }
  html, body { width: 1200px; height: 900px; overflow: hidden; }
  body {
    background: var(--bg);
    font-family: "Montserrat", sans-serif;
    position: relative;
  }
  .card {
    position: absolute;
    left: 260px;
    width: 680px;
    height: 388px;
    background: var(--card);
    border-radius: 26px;
    overflow: hidden;
    box-shadow: 0 10px 30px rgba(0,0,0,0.12);
  }
  .card--back { top: 40px; }
  .card--front { top: 472px; }
  .card__waves { position: absolute; inset: 0; width: 100%; height: 100%; }

  .brand {
    position: absolute;
    display: flex;
    align-items: center;
    gap: 16px;
    z-index: 1;
  }
  .brand__dot {
    width: 52px; height: 52px;
    border-radius: 50%;
    background: var(--green-light);
    flex: none;
  }
  .brand__name {
    font-weight: 700;
    color: var(--ink);
    line-height: 1.05;
    white-space: nowrap;
  }
  .brand__name span { display: block; }
  .card--back .brand { left: 90px; top: 100px; }
  .card--back .brand__name { font-size: 38px; }
  .card--front .brand { left: 70px; top: 214px; gap: 12px; }
  .card--front .brand__dot { width: 34px; height: 34px; }
  .card--front .brand__name { font-size: 22px; }

  .holder {
    position: absolute;
    right: 48px;
    top: 38px;
    text-align: right;
    z-index: 1;
  }
  .holder__name {
    font-family: "Rochester", cursive;
    font-size: 54px;
    color: var(--ink);
    line-height: 1;
  }
  .holder__role {
    font-size: 13px;
    font-weight: 500;
    color: var(--ink-soft);
    letter-spacing: 0.5px;
    margin-top: 4px;
  }
  .contact {
    position: absolute;
    right: 48px;
    top: 140px;
    list-style: none;
    text-align: right;
    font-size: 13px;
    color: var(--ink-soft);
    line-height: 1.6;
    z-index: 1;
  }
  .contact__label { font-weight: 500; color: var(--ink); }
</style>
</head>
<body>

  <section class="card card--back" aria-label="Back of card">
    <svg class="card__waves" viewBox="0 0 680 388" preserveAspectRatio="none" aria-hidden="true">
      <path d="M0,388 L0,350 C200,345 360,300 460,220 C540,155 610,110 680,95 L680,388 Z" fill="var(--green-light)"/>
      <path d="M0,388 L0,362 C210,358 380,312 480,236 C560,176 620,138 680,124 L680,388 Z" fill="#ffffff"/>
      <path d="M200,340 C330,320 420,276 500,214 C570,160 630,122 680,110 L680,130 C630,142 570,182 500,236 C420,294 330,332 200,340 Z" fill="var(--green)"/>
      <path d="M0,388 L0,372 C180,370 320,342 420,308 C520,272 600,262 680,260 L680,388 Z" fill="#ffffff"/>
      <path d="M0,372 C180,370 320,342 420,308 C520,272 600,262 680,260 L680,274 C600,276 520,286 420,320 C320,354 180,382 0,388 Z" fill="var(--green-deep)"/>
    </svg>
    <div class="brand">
      <span class="brand__dot"></span>
      <p class="brand__name"><span>Willowbend</span><span>Pharmacy</span></p>
    </div>
  </section>

  <section class="card card--front" aria-label="Front of card">
    <svg class="card__waves" viewBox="0 0 680 388" preserveAspectRatio="none" aria-hidden="true">
      <path d="M150,388 C210,300 330,290 470,280 C580,272 650,240 680,200 L680,388 Z" fill="var(--pink)"/>
      <path d="M170,388 C240,330 350,318 480,306 C590,296 650,270 680,236 L680,388 Z" fill="var(--pink-deep)"/>
      <path d="M200,388 C270,348 380,340 500,330 C600,322 655,300 680,272 L680,388 Z" fill="#ffffff"/>
      <path d="M220,388 C290,360 390,352 510,344 C610,336 660,316 680,290" fill="none" stroke="var(--pink-soft)" stroke-width="1" stroke-dasharray="3 3"/>
    </svg>
    <div class="holder">
      <p class="holder__name">Dorian Kessel</p>
      <p class="holder__role">Pharmacy Manager</p>
    </div>
    <ul class="contact">
      <li><span class="contact__label">P:</span> +1 555-014-2290</li>
      <li><span class="contact__label">E:</span> dorian@willowbendpharmacy.example</li>
      <li><span class="contact__label">W:</span> www.willowbendpharmacy.example</li>
    </ul>
    <div class="brand">
      <span class="brand__dot"></span>
      <p class="brand__name"><span>Willowbend</span><span>Pharmacy</span></p>
    </div>
  </section>

</body>
</html>
```